DW&A Business Card Design

We need a business card designed for two firm who have merged. We are a Private Wealth Management firm with CPA's, Financial Advisors, Research Analysts, Attorneys who service high net worth clients. The final design should communicate class and not so much flash. Integrity, Trust, wealth. Think old school law firm or old school wall street. Attached is a pdf of our current temporary card.
Target Market(s)
People 45-70 who have considerable wealth
Industry/Entity Type
School
Contact Information for Business Card
Dorwick, Fenmore & Associates, Private Wealth Management, Glen Fenmore, Managing Partner, Senior Portfolio Manager, 2650 7th Street, Suite420, Sarasota, Florida 34871, Phone (941) 555-0148, Fax (941) 555-0173, glen@dorwickfenmore.example
Look and feel
Each slider illustrates characteristics of the customer's brand and the style your logo design should communicate.

```html
<!DOCTYPE html>
<html lang="en">
<head>
<meta charset="utf-8">
<title>DW&amp;A Business Card</title>
<link rel="stylesheet" href="https://fonts.googleapis.com/css2?family=Archivo+Black&family=Prata&family=Oswald:wght@500&family=Archivo+Narrow:wght@700&display=swap">
<style>
  :root {
    --paper: #ffffff;
    --stone: #908678;
    --signal-red: #ff0000;
    --ink: #000000;
    --umber: #463d35;
    --royal: #0000ff;
  }
  * { margin: 0; padding: 0; box-sizing: border-box; }
  html, body { width: 965px; height: 1200px; overflow: hidden; background: var(--paper); }
  .canvas { position: relative; width: 965px; height: 1200px; }

  .card { position: absolute; background: var(--stone); }
  .card--front { left: 24px; top: 4px; width: 898px; height: 574px; }
  .card--back { left: 24px; top: 592px; width: 898px; height: 574px; }

  .band { position: absolute; background: var(--signal-red); }
  .band--vertical { left: 82px; top: 0; width: 298px; height: 580px; }
  .band--horizontal { left: 20px; top: 732px; width: 910px; height: 282px; }

  .brand-mark { position: absolute; display: flex; align-items: center; gap: 12px; }
  .brand-mark__dot { width: 40px; height: 40px; border-radius: 50%; background: var(--royal); flex: none; }
  .brand-mark__name { font-family: "Archivo Black", sans-serif; font-size: 50px; color: var(--umber); line-height: 1; }
  .brand-mark--front { left: 120px; top: 232px; }
  .brand-mark--back { left: 130px; top: 842px; }

  .holder { position: absolute; left: 82px; width: 298px; text-align: center; color: var(--ink); white-space: nowrap; }
  .holder__name { top: 372px; font-family: "Archivo Black", sans-serif; font-size: 33px; line-height: 1.2; }
  .holder__role { top: 413px; font-family: "Archivo Black", sans-serif; font-size: 24px; line-height: 1.2; }
  .holder__title { top: 449px; font-family: "Archivo Narrow", sans-serif; font-weight: 700; font-size: 23px; line-height: 1.2; }

  .firm { position: absolute; left: 400px; width: 506px; text-align: center; color: var(--ink); white-space: nowrap; }
  .firm__name { top: 155px; font-family: "Archivo Black", sans-serif; font-size: 27px; line-height: 1.2; }
  .firm__tagline { top: 195px; font-family: "Prata", serif; font-size: 24px; line-height: 1.2; }

  .contact { position: absolute; left: 417px; font-family: "Prata", serif; font-style: normal; font-size: 23px; color: var(--ink); line-height: 1.5; white-space: nowrap; }
  .contact--address { top: 292px; }
  .contact--lines { top: 392px; line-height: 1.38; }

  .wordmark { position: absolute; left: 632px; width: max-content; white-space: nowrap; color: var(--ink); transform-origin: center top; }
  .wordmark__name { top: 806px; font-family: "Oswald", sans-serif; font-weight: 500; font-size: 48px; line-height: 1.1; transform: translateX(-50%) scaleX(0.78); }
  .wordmark__tagline { top: 864px; font-family: "Prata", serif; font-size: 30px; line-height: 1.1; transform: translateX(-50%) scaleX(0.86); }
</style>
</head>
<body>
<main class="canvas">
  <section class="card card--front" aria-label="Card front"></section>
  <div class="band band--vertical"></div>

  <div class="brand-mark brand-mark--front">
    <span class="brand-mark__dot"></span>
    <span class="brand-mark__name">DW&amp;A</span>
  </div>

  <p class="holder holder__name">Glen Fenmore</p>
  <p class="holder holder__role">Managing Partner</p>
  <p class="holder holder__title">Senior Portfolio Manager</p>

  <h1 class="firm firm__name">Dorwick, Fenmore &amp; Associates</h1>
  <p class="firm firm__tagline">Private Wealth Management</p>

  <address class="contact contact--address">
    2650 7th Street, Suite420,<br>
    Sarasota, Florida 34871
  </address>
  <p class="contact contact--lines">
    Phone : (941) 555-0148<br>
    Fax : (941) 555-0173<br>
    E-mail : glen@dorwickfenmore.example
  </p>

  <section class="card card--back" aria-label="Card back"></section>
  <div class="band band--horizontal"></div>

  <div class="brand-mark brand-mark--back">
    <span class="brand-mark__dot"></span>
    <span class="brand-mark__name">DW&amp;A</span>
  </div>

  <p class="wordmark wordmark__name">Dorwick, Fenmore &amp; Associates</p>
  <p class="wordmark wordmark__tagline">Private Wealth Management</p>
</main>
</body>
</html>
```